Canned Olive & Fish Fusion Label Design

We are seeking a high-quality, premium label design for our Corlina Bay Medley product line. The visual identity should integrate a maritime theme, using a pattern inspired by a boat anchor and a boat. The background should be primarily purple, reflecting elegance and product distinction.
The Pasko logo must remain centered, prominent, and clearly visible.

Product Flavors:

-Anchovy

-Shrimp

Design Requirements:

Include real or illustrated, appetizing visuals for both varieties:

-Olives combined with anchovy

-Olives combined with shrimp

All product information must appear in bilingual format (French & English).

Ingredients: Olives, salt, water, fish extract.

Packaging size: 7 cm × 14.5 cm,
140 g.
The barcode must be on the label, along with the nutrition facts.

Use distinct text colors or visual accents to clearly differentiate each flavor while keeping the overall branding cohesive.

Ensure the label style is unique, modern, and highly eye-catching, suitable for a premium gourmet product.

I’m sharing some ideas with you, along with the pictures I’ve attached.
We are looking for a creative, polished, and visually striking label
concept that showcases the maritime inspiration, enhances the product’s gourmet quality, and stands out on retail shelves.

Target Market(s)

Americans and Mediterranean consumers

Industry/Entity Type

Food

Colors
EE7325
F08F49
F5BC92
FAE3D3
FDF4ED
EB3D1F
EC4F4E
F09395
F8D3D4
FCEDEE
E54698
E96AAD
F1A4CE
F9D9EA
FCEFF6
A7469A
B969AE
D3A5CF
EDDBEB
F8F0F9
6B429C
8869AF
B7A5CE
E3DAEB
F3F0F8

Requirements
Must have
• 2 labels :Olives + anchovy Olives + shrimp
Nice to have
• Shadow or 3D effects to make the images or text pop. Small serving suggestion icons (e.g., tapas, salad, appetizer).

```html
<!DOCTYPE html>
<html lang="fr">
<head>
<meta charset="utf-8">
<title>Pasko – Corlina Bay Medley labels</title>
<link rel="stylesheet" href="https://fonts.googleapis.com/css2?family=Barlow+Condensed:wght@400;500&family=Oswald:wght@500;600&family=Open+Sans:wght@700&display=swap">
<style>
  :root{
    --canvas:#e8e8e8;
    --navy:#25215a;
    --navy-deep:#1d1a4d;
    --coral:#ee4035;
    --title-red:#e8412f;
    --white:#ffffff;
    --ink:#111111;
    --olive:#9da82c;
    --leaf:#2f6b2a;
    --shrimp:#f0603a;
    --fish:#5a6c80;
  }
  *{box-sizing:border-box;margin:0;padding:0}
  html,body{width:1200px;height:960px;overflow:hidden;background:var(--canvas)}
  .sheet{position:relative;width:1200px;height:960px;background:var(--canvas)}
  .label{position:absolute;left:165px;width:882px;height:426px;color:var(--white)}
  .label--shrimp{top:40px;background:var(--navy)}
  .label--anchovy{top:486px;background:var(--coral)}

  .nutrition{position:absolute;left:76px;top:62px;width:268px;border-collapse:collapse;
    font-family:"Barlow Condensed",sans-serif;font-weight:500;font-size:15px;line-height:19px}
  .nutrition th,.nutrition td{border:1.5px solid var(--white);padding:0 6px;vertical-align:middle}
  .nutrition .title-cell{border:none;text-align:left;font-weight:500;font-size:15px;line-height:19.5px;vertical-align:top;padding:0}
  .nutrition .unit-cell{text-align:right;font-weight:500;height:54px;padding-right:5px}
  .nutrition td:first-child{width:156px}
  .nutrition td:last-child{text-align:center}
  .row-energy td{height:29px}
  .row-fat td,.row-carb td{height:46px}
  .row-fibre td,.row-protein td,.row-salt td{height:23px}

  .barcode-slot{position:absolute;left:113px;top:327px;width:194px;height:68px;background:var(--white);
    display:flex;align-items:center;justify-content:center;
    font-family:"Open Sans",sans-serif;font-weight:700;font-size:20px;color:var(--ink);letter-spacing:-.3px}

  .brand{position:absolute;left:560px;top:62px;width:200px;text-align:center;
    font-family:"Oswald",sans-serif;font-weight:600;font-size:50px;line-height:60px;color:var(--white);letter-spacing:1px}

  .product-name{position:absolute;left:510px;top:136px;width:300px;text-align:center;
    font-family:"Oswald",sans-serif;font-weight:600;font-size:34px;line-height:37px;text-transform:uppercase;letter-spacing:.3px}
  .label--shrimp .product-name{color:var(--title-red)}
  .label--anchovy .product-name{color:var(--white)}

  .serving-visual{position:absolute;left:514px;top:258px;width:258px;height:134px}
  .weight{position:absolute;left:594px;top:384px;width:70px;text-align:center;
    font-family:"Open Sans",sans-serif;font-weight:700;font-size:19px;color:var(--white)}
</style>
</head>
<body>
<main class="sheet">

  <section class="label label--shrimp">
    <table class="nutrition">
      <tr><th class="title-cell">VALEURS<br>NUTRITIONNELLES<br>MOYENNES</th><th class="unit-cell">pour 100 g de<br>prodait egoutte</th></tr>
      <tr class="row-energy"><td>Energie</td><td>634 J - 154 kcal</td></tr>
      <tr class="row-fat"><td>Matieres grasses<br>dont saturees</td><td>16g<br>3g</td></tr>
      <tr class="row-carb"><td>Glucides<br>dont sucres</td><td>0g<br>0g</td></tr>
      <tr class="row-fibre"><td>Fibres</td><td>2.5 g</td></tr>
      <tr class="row-protein"><td>Proteines</td><td>1.3 g</td></tr>
      <tr class="row-salt"><td>Sel</td><td>3 g</td></tr>
    </table>
    <div class="barcode-slot">BAR CODE</div>
    <div class="brand">PASKO</div>
    <h2 class="product-name">Corlina Bay<br>Medley<br>Gout Crevette</h2>
    <svg class="serving-visual" viewBox="0 0 258 134" role="img" aria-label="Green olives with leaves and a cooked shrimp">
      <defs><linearGradient id="shrimpTone" x1="0" y1="0" x2="1" y2="1">
        <stop offset="0" stop-color="#a8b23a"/><stop offset=".55" stop-color="#7f9a2a"/><stop offset="1" stop-color="#f0603a"/></linearGradient></defs>
      <ellipse cx="129" cy="72" rx="126" ry="60" fill="url(#shrimpTone)"/>
    </svg>
    <div class="weight">140 g</div>
  </section>

  <section class="label label--anchovy">
    <table class="nutrition">
      <tr><th class="title-cell">VALEURS<br>NUTRITIONNELLES<br>MOYENNES</th><th class="unit-cell">pour 100 g de<br>prodait egoutte</th></tr>
      <tr class="row-energy"><td>Energie</td><td>634 J - 154 kcal</td></tr>
      <tr class="row-fat"><td>Matieres grasses<br>dont saturees</td><td>16g<br>3g</td></tr>
      <tr class="row-carb"><td>Glucides<br>dont sucres</td><td>0g<br>0g</td></tr>
      <tr class="row-fibre"><td>Fibres</td><td>2.5 g</td></tr>
      <tr class="row-protein"><td>Proteines</td><td>1.3 g</td></tr>
      <tr class="row-salt"><td>Sel</td><td>3 g</td></tr>
    </table>
    <div class="barcode-slot">BAR CODE</div>
    <div class="brand">PASKO</div>
    <h2 class="product-name">Corlina Bay<br>Medley<br>Gout Crevette</h2>
    <svg class="serving-visual" viewBox="0 0 258 134" role="img" aria-label="Green olives with leaves and an anchovy">
      <defs><linearGradient id="fishTone" x1="0" y1="0" x2="1" y2="1">
        <stop offset="0" stop-color="#a8b23a"/><stop offset=".55" stop-color="#7f9a2a"/><stop offset="1" stop-color="#5a6c80"/></linearGradient></defs>
      <ellipse cx="129" cy="72" rx="126" ry="60" fill="url(#fishTone)"/>
    </svg>
    <div class="weight">140 g</div>
  </section>

</main>
</body>
</html>
```